Unique business card design

Boutique coastal hotel suites - in need of clever stand out business card I have uploaded the logo that I had created through quill forge I want something that is clever and stands out from everyone else - 418 Brantwell Avenue seldovia Alaska 99571 phone or text 907 -581-6142 www.primemarrowbysuites.com

Target Market(s)

Men and woman

Industry/Entity Type

Boutique coastal hotel

Contact Information for Business Card

Marrowby Suites Halvern Bay Alaska marrowby_suites@mailnest.net

Requirements
Must have
• Classy - clever -bold 907-581-6142 call or text

```html
<!DOCTYPE html>
<html lang="en">
<head>
<meta charset="utf-8">
<title>Marrowby Suites – Business Card</title>
<link href="https://fonts.googleapis.com/css2?family=Arimo:wght@400;700&display=swap" rel="stylesheet">
<style>
  :root {
    --bg: #2a2a2b;
    --card: #0d0d0e;
    --navy: #34577a;
    --red: #d6262b;
    --yellow: #f2c21b;
    --white: #f4f4f4;
    --rule: #2b2b2e;
  }
  * { box-sizing: border-box; margin: 0; padding: 0; }
  html, body { width: 1200px; height: 900px; overflow: hidden; }
  body {
    background: var(--bg);
    font-family: "Arimo", Arial, sans-serif;
    display: flex;
    flex-direction: column;
    align-items: center;
    justify-content: center;
    gap: 56px;
  }
  .card {
    width: 630px;
    height: 360px;
    background: var(--card);
    border-radius: 22px;
    position: relative;
    box-shadow: 0 14px 30px rgba(0,0,0,.55);
  }
  .brand {
    display: flex;
    align-items: center;
    gap: 14px;
    color: var(--navy);
    font-weight: 700;
    text-transform: uppercase;
    letter-spacing: .08em;
    white-space: nowrap;
  }
  .brand-mark { width: 18px; height: 18px; background: var(--red); flex: none; }
  .card-back { display: flex; align-items: center; justify-content: center; }
  .card-back .brand { font-size: 38px; }
  .card-front { display: flex; }
  .front-brand {
    width: 46%;
    flex: none;
    display: flex;
    align-items: center;
    justify-content: center;
    border-right: 1px solid var(--rule);
    padding: 0 16px;
  }
  .front-brand .brand { font-size: 19px; gap: 9px; letter-spacing: .06em; }
  .front-brand .brand-mark { width: 12px; height: 12px; }
  .contact { padding: 62px 0 0 34px; color: var(--white); }
  .person-name { color: var(--navy); font-size: 22px; text-transform: uppercase; letter-spacing: .02em; }
  .person-role { color: var(--red); font-size: 15px; text-transform: uppercase; margin: 2px 0 16px; }
  .contact-list { list-style: none; font-size: 15px; line-height: 1.55; }
  .contact-list li { display: flex; align-items: center; gap: 9px; white-space: nowrap; }
  .contact-list svg { width: 14px; height: 14px; flex: none; }
  .call-note { color: var(--yellow); }
  .address { font-size: 15px; line-height: 1.45; margin: 16px 0 0 23px; }
</style>
</head>
<body>
  <section class="card card-back">
    <div class="brand"><span class="brand-mark"></span>Marrowby Suites</div>
  </section>

  <section class="card card-front">
    <div class="front-brand">
      <div class="brand"><span class="brand-mark"></span>Marrowby Suites</div>
    </div>
    <div class="contact">
      <h1 class="person-name">Everett Lindqvist</h1>
      <p class="person-role">Managing Director</p>
      <ul class="contact-list">
        <li>
          <svg viewBox="0 0 16 16" fill="var(--navy)"><path d="M3.5 1l2.5 3-1.5 1.8c.9 2 2.4 3.6 4.5 4.6L10.8 9l3.2 2.4-1.3 2.9C7 14 2 9 1.7 3.2z"/></svg>
          <span>907 -581-6142 ( <span class="call-note">Call or text</span> )</span>
        </li>
        <li>
          <svg viewBox="0 0 16 16" fill="none" stroke="var(--navy)" stroke-width="1.6"><rect x="1" y="3" width="14" height="10"/><path d="M1 3l7 6 7-6"/></svg>
          <span>marrowby_suites@mailnest.net</span>
        </li>
        <li>
          <svg viewBox="0 0 16 16" fill="none" stroke="var(--navy)" stroke-width="1.4"><circle cx="8" cy="8" r="6.5"/><ellipse cx="8" cy="8" rx="3" ry="6.5"/><path d="M1.5 8h13M3 4.5h10M3 11.5h10"/></svg>
          <span>www.primemarrowbysuites.com</span>
        </li>
      </ul>
      <p class="address">418 Brantwell Avenue<br>halvern bay Alaska 99571</p>
    </div>
  </section>
</body>
</html>
```